LUMO - Óptica Clarena - web design and concept

Website concept - Create and develop our website design and structure. LUMO is an optical store chain, and we are looking to establish our web and digital concept. In attachment there are several pictures about our stores and our logo.

The website structure should be user friendly. Colors should be light and the design as simple and minimalist as possible. There are different variations of the logothat can be used, check the file.

The website will include optical collections and sun collections as an online store. Also, a medical menu should be considered in order for clients to schedule optometry appointments. There should also be a menu for client assistance where the clients can read about glass maintenance in our workshop.

Number of Pages Required

5+ page

Font styles to use
Serif
Sans Serif

Requirements
Must have
• Must be user-friendly and minimalist.
• Please USE PICTURES FROM THE BRANDS we sell: BRELO, MORVE, PKS, KOSU, NERAP
Nice to have
• Nice to inspire: ZEB glasses (see website https://ch.shopzeb-example.com/en/)
• Nice to inspire: https://brelo-eyewear-example.com/
• Nice to ispire: https://www.pksplanet-example.com/en/
Should not have
• Hysteric colors and shapes

```html
<!DOCTYPE html>
<html lang="es">
<head>
<meta charset="utf-8">
<title>LUMO · Óptica Clarena</title>
<link rel="stylesheet" href="https://fonts.googleapis.com/css2?family=Montserrat:wght@300;400;500;600&family=Open+Sans:wght@400;600;700&display=swap">
<style>
:root{
  --gold:#d8a74a;
  --gold-light:#e6bf6c;
  --gold-deep:#c8943a;
  --ink:#151515;
  --text:#333;
  --line:#e4e4e4;
  --paper:#fff;
  --grey-bg:#efefef;
  --star:#d8a74a;
}
*{box-sizing:border-box;margin:0;padding:0}
html,body{width:1200px;height:4296px;overflow:hidden}
body{font-family:"Open Sans",Arial,sans-serif;color:var(--text);background:var(--paper);position:relative}
h1,h2,h3{font-family:"Montserrat",Helvetica,sans-serif;font-weight:300}

/* header */
.site-header{position:absolute;left:0;top:0;width:1200px;height:123px;background:var(--gold)}
.brand-box{position:absolute;left:95px;top:0;width:211px;height:130px;background:var(--ink);display:flex;flex-direction:column;align-items:center;justify-content:center;box-shadow:0 4px 10px rgba(0,0,0,.25)}
.brand-name{font-family:"Montserrat",sans-serif;font-weight:400;font-size:42px;letter-spacing:8px;color:var(--gold)}
.brand-sub{font-family:"Montserrat",sans-serif;font-weight:400;font-size:12px;letter-spacing:3px;color:var(--gold);margin-top:2px}
.search{position:absolute;left:558px;top:28px;width:315px;height:30px;display:flex}
.search-field{flex:1;background:var(--gold-light);border:1px solid #b98c35;font-size:11px;color:#5a4520;padding:8px 10px}
.search-btn{width:96px;background:var(--ink);color:#fff;font-size:12px;font-family:"Montserrat",sans-serif;display:flex;align-items:center;justify-content:center;letter-spacing:1px}
.cart{position:absolute;left:1028px;top:33px;display:flex;align-items:center;gap:10px;font-size:12px;color:var(--ink);font-family:"Montserrat",sans-serif}
.main-nav{position:absolute;right:88px;top:80px;display:flex;gap:22px;font-family:"Montserrat",sans-serif;font-size:13px;font-weight:500;letter-spacing:1px;color:var(--ink)}

/* hero */
.hero{position:absolute;left:0;top:123px;width:1200px;height:473px;background:linear-gradient(100deg,#e9eef2 0%,#cfdbe4 30%,#8fb3c8 52%,#c9a488 70%,#efe7df 100%)}
.hero-title{position:absolute;left:115px;top:150px;font-size:46px;line-height:54px;letter-spacing:3px;color:#fff;font-weight:400;text-shadow:0 1px 4px rgba(0,0,0,.25)}
.hero-title em{font-style:normal;color:var(--gold)}
.btn-dark{position:absolute;background:var(--ink);color:var(--gold);font-family:"Montserrat",sans-serif;font-size:15px;letter-spacing:2px;display:flex;align-items:center;justify-content:center}
.btn-dark::before,.btn-dark::after{content:"";position:absolute;width:16px;height:16px;border:2px solid var(--gold)}
.btn-dark::before{left:-4px;top:-4px;border-right:none;border-bottom:none}
.btn-dark::after{right:-4px;bottom:-4px;border-left:none;border-top:none}

/* about */
.about-photo{position:absolute;left:86px;top:667px;width:490px;height:479px;background:linear-gradient(90deg,#2d2a26 0%,#4f8b9e 25%,#2f2a24 45%,#5a9bae 65%,#e2d3bd 100%)}
.about-card{position:absolute;left:487px;top:696px;width:630px;height:415px;background:#fff;box-shadow:0 6px 24px rgba(0,0,0,.15);text-align:center;padding:110px 60px 0}
.about-card h2{font-size:34px;letter-spacing:3px;color:var(--gold)}
.about-card p{font-size:13px;line-height:25px;color:#444;margin-top:18px}

/* how we work */
.how{position:absolute;left:0;top:1214px;width:1200px;height:519px;background:linear-gradient(180deg,#1c1e20,#2b3234 50%,#191a1b)}
.how h2{position:absolute;left:0;width:1200px;top:60px;text-align:center;font-size:40px;color:#fff;letter-spacing:3px}
.how-col{position:absolute;top:150px;width:320px;height:340px;text-align:center;color:#eee;font-size:13px;line-height:25px}
.how-col svg{display:block;margin:0 auto 22px}
.how-divider{position:absolute;top:150px;width:1px;height:330px;background:rgba(255,255,255,.35)}

/* products intro */
.section-title{position:absolute;left:0;width:1200px;text-align:center;font-size:40px;letter-spacing:3px;color:var(--ink)}
.tabs{position:absolute;left:0;width:1200px;top:1862px;text-align:center;font-size:11px;letter-spacing:1px;color:#666;font-family:"Montserrat",sans-serif}
.tabs b{font-weight:600;color:var(--ink)}
.tabs span.sep{margin:0 8px}
.tab-caret{position:absolute;left:230px;top:1882px}
.feature-text{position:absolute;left:86px;top:1962px;width:520px;font-size:14px;line-height:26px;color:#333}
.feature-text h3{font-size:24px;color:var(--gold);font-weight:400;margin-bottom:18px}
.feature-text p+p{margin-top:26px}
.feature-photo{position:absolute;left:610px;top:1933px;width:507px;height:321px;background:linear-gradient(90deg,#f1f1ef 0%,#d9d4cc 40%,#8a6a52 60%,#4d7a45 85%,#2f5a2c 100%)}

/* products grid */
.products-band{position:absolute;left:0;top:2320px;width:1200px;height:659px;background:var(--grey-bg)}
.product{position:absolute;top:2443px;width:328px}
.product-photo{height:226px;background:#fff;display:flex;align-items:center;justify-content:center;position:relative}
.product-photo .ph{width:260px;height:120px;background:linear-gradient(180deg,#f4f4f4,#dcdcdc);border-radius:40px}
.product-actions{position:absolute;right:26px;bottom:28px;display:flex;gap:8px}
.product-actions span{width:34px;height:34px;display:flex;align-items:center;justify-content:center}
.product h3{font-family:"Open Sans",sans-serif;font-weight:600;font-size:21px;color:var(--ink);margin:20px 0 8px 18px}
.product p{font-size:13px;line-height:20px;color:#444;margin-left:18px;width:280px}
.stars{margin:8px 0 0 18px;font-size:12px;color:var(--star);letter-spacing:1px}
.stars i{font-style:normal;color:#ccc}
.price{margin:10px 0 0 18px;display:flex;align-items:baseline;gap:12px}
.price s{font-size:13px;color:#888}
.price strong{font-size:26px;font-weight:400;color:var(--gold);font-family:"Montserrat",sans-serif}

/* brands */
.brands{position:absolute;left:0;top:2979px;width:1200px;height:300px;background:linear-gradient(120deg,var(--gold-deep),var(--gold-light) 45%,var(--gold) 70%,var(--gold-deep))}
.brands h2{position:absolute;left:0;width:1200px;top:58px;text-align:center;color:#fff;font-size:40px;letter-spacing:3px}
.brand-tile{position:absolute;top:128px;width:186px;height:100px;background:#fff;display:flex;align-items:center;justify-content:center;font-family:"Open Sans",sans-serif;font-weight:700;font-size:20px;letter-spacing:2px;color:var(--ink)}

/* blog */
.post-img{position:absolute;width:329px;height:244px}
.post-card{position:absolute;background:#fff;border:1px solid var(--line);padding:22px 20px}
.post-card h3{font-family:"Open Sans",sans-serif;font-weight:600;font-size:20px;line-height:27px;color:var(--ink)}
.post-card p{font-size:12px;line-height:19px;color:#555;margin-top:12px}
.post-card a{color:var(--gold);text-decoration:none}

/* footer */
.site-footer{position:absolute;left:0;top:3995px;width:1200px;height:301px;background:#111;color:#ddd}
.f-title{position:absolute;top:70px;font-family:"Montserrat",sans-serif;font-size:20px;color:var(--gold)}
.f-list{position:absolute;top:110px;list-style:none;font-size:13px;line-height:17px;color:#ccc}
.f-email{position:absolute;left:86px;top:112px;width:238px;height:38px;border:1px solid #aaa;font-size:12px;color:#aaa;padding:10px 12px}
.f-btn{position:absolute;left:86px;top:162px;width:238px;height:38px;background:var(--gold);color:var(--ink);font-family:"Montserrat",sans-serif;font-size:14px;letter-spacing:2px;display:flex;align-items:center;justify-content:center}
.f-brand{position:absolute;left:880px;top:60px;text-align:center;width:240px}
.f-brand .brand-name{font-size:40px}
.f-social{display:flex;gap:10px;justify-content:center;margin-top:18px}
.f-social span{width:28px;height:28px;border:2px solid var(--gold);border-radius:50%}
.f-copy{margin-top:20px;font-size:12px;color:#ccc}
</style>
</head>
<body>

<header class="site-header">
  <div class="brand-box">
    <div class="brand-name">LUMO</div>
    <div class="brand-sub">Óptica Clarena</div>
  </div>
  <div class="search"><div class="search-field">Search...</div><div class="search-btn">SEARCH</div></div>
  <div class="cart">
    <svg width="28" height="22" viewBox="0 0 28 22" fill="none" stroke="#151515" stroke-width="2"><path d="M1 2h5l3 12h14l3-9H8"/><circle cx="11" cy="19" r="2"/><circle cx="21" cy="19" r="2"/></svg>
    CART (0)
  </div>
  <nav class="main-nav"><span>INICO</span><span>QUIENES SOMOS</span><span>PRODUCTOS</span><span>CITA ÓPTICA</span><span>CONTACTO</span><span>BLOG</span><span>TIENDA</span></nav>
</header>

<section class="hero" role="img" aria-label="Pareja sonriente con gafas de sol junto al mar">
  <h1 class="hero-title">ENJOY THE WORLD<br>WITH <em>LUMO</em> GLASSES</h1>
  <div class="btn-dark" style="left:115px;top:277px;width:235px;height:36px">EXPLORE NOW</div>
</section>

<section class="about">
  <div class="about-photo" role="img" aria-label="Interior de una tienda LUMO con vitrinas iluminadas"></div>
  <div class="about-card">
    <h2>LUMO ÓPTICA CLARENA</h2>
    <p>Lorem Ipsum is simply dummy text of the printing and typesetting industry. Lorem Ipsum has been the industry's standard dummy text ever since the 1500s, when an unknown printer took a galley of type and scrambled it to make a type specimen book. It has survived not only five centuries, but also the leap into electronic typesetting, remaining essentially unchanged.</p>
  </div>
  <div class="btn-dark" style="left:683px;top:1020px;width:238px;height:38px">READ MORE</div>
</section>

<section class="how">
  <h2>¿CÓMO TRABAJAMOS?</h2>
  <div class="how-col" style="left:95px">
    <svg width="110" height="62" viewBox="0 0 110 62"><path d="M2 2h106L55 60z" fill="none" stroke="#d8a74a" stroke-width="2"/><text x="55" y="34" text-anchor="middle" fill="#d8a74a" font-family="Montserrat" font-size="26">1</text></svg>
    En LUMO Óptica cada paciente es único. Te ofrecemos un asesoramiento cercano y profesional, recomendando la solución visual que más se adapte a ti y a tu vida diaria. Desde lentes de contacto hasta gafas progresivas, trabajamos por y para ti.
  </div>
  <div class="how-divider" style="left:425px"></div>
  <div class="how-col" style="left:440px">
    <svg width="110" height="62" viewBox="0 0 110 62"><path d="M2 2h106L55 60z" fill="none" stroke="#d8a74a" stroke-width="2"/><text x="55" y="34" text-anchor="middle" fill="#d8a74a" font-family="Montserrat" font-size="26">2</text></svg>
    Como la calidad es el sello de nuestro trabajo, disponemos de las mejores marcas del mercado. Como Zendra, líder mundial en fabricación de lentes ópticas de precisión. Aquivo, de Jonas &amp; Jonas, tiene tal confianza en sus productos que garantiza la devolución del importe si el usuario no está plenamente satisfecho.
  </div>
  <div class="how-divider" style="left:775px"></div>
  <div class="how-col" style="left:790px">
    <svg width="110" height="62" viewBox="0 0 110 62"><path d="M2 2h106L55 60z" fill="none" stroke="#d8a74a" stroke-width="2"/><text x="55" y="34" text-anchor="middle" fill="#d8a74a" font-family="Montserrat" font-size="26">3</text></svg>
    Prueba a graduarte con nuestro completo sistema de análisis visual, con el que en tan solo 45 minutos podrás tener una idea del estado exacto de tu visión. Pide cita aquí mismo.
  </div>
</section>

<h2 class="section-title" style="top:1790px">NUESTROS PRODUCTOS</h2>
<div class="tabs"><b>MONTURA GRADUADA</b><span class="sep">/</span>ESPECIAL NIÑOS<span class="sep">/</span>LENTES OFTÁLMICAS<span class="sep">/</span>GAFA SOL<span class="sep">/</span>LENTES DE CONTACTO<span class="sep">/</span>BAJA VISIÓN<span class="sep">/</span>OTROS PRODUCTOS</div>
<svg class="tab-caret" width="14" height="9" viewBox="0 0 14 9"><path d="M1 1l6 6 6-6" fill="none" stroke="#151515" stroke-width="2"/></svg>
<div class="feature-text">
  <h3>Montura Graduada</h3>
  <p>Disponemos de una selección de monturas de las mejores marcas: MORVE, KOSU, PKS, NERAP, BRELO...</p>
  <p>Para los seguidores de las últimas tendencias y para los más clásicos, en LUMO Óptica encontraremos la gafa que más se adapte a tu estilo y personalidad.</p>
</div>
<div class="btn-dark" style="left:86px;top:2167px;width:238px;height:38px">READ MORE</div>
<div class="feature-photo" role="img" aria-label="Mujer con gafas graduadas junto a una ventana y una planta"></div>

<section class="products-band"></section>
<h2 class="section-title" style="top:2375px">PRODUCTOS</h2>

<article class="product" style="left:86px">
  <div class="product-photo" role="img" aria-label="Gafas graduadas de montura metálica"><div class="ph"></div>
    <div class="product-actions">
      <span style="background:#151515"><svg width="14" height="14" viewBox="0 0 14 14"><circle cx="7" cy="7" r="6" fill="none" stroke="#fff" stroke-width="2"/><circle cx="7" cy="7" r="2" fill="#fff"/></svg></span>
      <span style="background:#d8a74a"><svg width="16" height="14" viewBox="0 0 16 14" fill="none" stroke="#fff" stroke-width="2"><path d="M1 1h3l2 8h8l1-6H5"/></svg></span>
    </div>
  </div>
  <h3>Lorem ipsum</h3>
  <p>Lorem Ipsum is simply dummy text of the printing and typesetting industry.</p>
  <div class="stars">★★★★<i>★</i></div>
  <div class="price"><s>£350</s><strong>£300</strong></div>
</article>
<article class="product" style="left:438px">
  <div class="product-photo" role="img" aria-label="Gafas graduadas de montura metálica"><div class="ph"></div></div>
  <h3>Lorem ipsum</h3>
  <p>Lorem Ipsum is simply dummy text of the printing and typesetting industry.</p>
  <div class="stars">★★★★<i>★</i></div>
  <div class="price"><s>£350</s><strong>£300</strong></div>
</article>
<article class="product" style="left:790px">
  <div class="product-photo" role="img" aria-label="Gafas graduadas de montura metálica"><div class="ph"></div></div>
  <h3>Lorem ipsum</h3>
  <p>Lorem Ipsum is simply dummy text of the printing and typesetting industry.</p>
  <div class="stars">★★★★<i>★</i></div>
  <div class="price"><s>£350</s><strong>£300</strong></div>
</article>
<div class="btn-dark" style="left:484px;top:2871px;width:234px;height:38px">VIEW MORE</div>

<section class="brands">
  <h2>BRANDS</h2>
  <div class="brand-tile" style="left:86px">BRELO</div>
  <div class="brand-tile" style="left:298px">MORVE</div>
  <div class="brand-tile" style="left:510px">PKS</div>
  <div class="brand-tile" style="left:720px">KOSU</div>
  <div class="brand-tile" style="left:931px">NERAP</div>
</section>

<h2 class="section-title" style="top:3332px">LATEST BLOG</h2>

<div class="post-img" style="left:86px;top:3408px;background:linear-gradient(120deg,#c9b2e6,#8e6fc4 50%,#e6d8f2)" role="img" aria-label="Vídeo sobre el ácido hialurónico y la salud visual"></div>
<article class="post-card" style="left:415px;top:3408px;width:347px;height:244px">
  <h3>¿El ácido hialurónico tiene que ver con la salud visual?</h3>
  <p>Seguro que el ácido hialurónico te suena, pero no lo asocies a la salud visual. Se suele hablar de él en cremas para la cara y antiarrugas. Pero, ¿realmente sabes lo que es? ¿Puedes imaginar qué relación tiene con tus ojos? ... <a>READ MORE</a></p>
</article>

<div class="post-img" style="left:86px;top:3675px;background:linear-gradient(120deg,#b9cfe0,#d27a5a 45%,#5aa9d6 75%,#e3d06a)" role="img" aria-label="Vídeo sobre cómo percibimos los colores"></div>
<article class="post-card" style="left:415px;top:3675px;width:347px;height:244px">
  <h3>¿De qué color son los plátanos?</h3>
  <p>Si normalmente sigues el canal del Óptico de ViewTube es probable que ya hayas visto el vídeo sobre el daltonismo. En él nuestro óptico hablaba del daltonismo, obvio, y para ello empezaba a tratar cómo se percibe el color ... <a>READ MORE</a></p>
</article>

<div class="post-img" style="left:790px;top:3408px;width:327px;background:linear-gradient(120deg,#d9c9b4,#8fb7d4 55%,#e6a0c8)" role="img" aria-label="Vídeo de opinión sobre gafas de sol para niños"></div>
<article class="post-card" style="left:790px;top:3652px;width:327px;height:266px;border-top:none">
  <h3>¿Debes poner gafas de sol a tus hijos?</h3>
  <p>En el último vídeo de El Óptico de ViewTube nuestro experto ha hablado sobre la importancia de utilizar gafas de sol durante todo el año, y protegerse bien los ojos. Uno de los temas que más preocupa a los padres es cuándo deben buscar una gafas de sol para niños. ¿A qué edad tienen su primer contacto? ... <a>READ MORE</a></p>
</article>

<footer class="site-footer">
  <div class="f-title" style="left:86px">Newsletter</div>
  <div class="f-email">Email...</div>
  <div class="f-btn">SUBSCRIBE</div>

  <div class="f-title" style="left:455px">Sitemap</div>
  <ul class="f-list" style="left:455px"><li>Inicio</li><li>Quienes Somos</li><li>Productos</li><li>Cita Óptica</li><li>Contacto</li><li>Blog</li><li>Tienda</li></ul>

  <div class="f-title" style="left:676px">Links</div>
  <ul class="f-list" style="left:676px"><li>Lorem</li><li>Ipsum</li><li>Simply</li><li>Dummy</li><li>Text</li><li>Printing</li></ul>

  <div class="f-brand">
    <div class="brand-name">LUMO</div>
    <div class="brand-sub">Óptica Clarena</div>
    <div class="f-social"><span></span><span></span><span></span></div>
    <div class="f-copy">Copyright © 2018 | All Rights Reserved.</div>
  </div>
</footer>

</body>
</html>
```